Vietnamese Restaurant Menu

We are an authentic Vietnamese noodle bar.

We would like our menu redesigned to become more attractive and have a picture for each item. We would like out new menu to look similar to the menu shown on the following website http://quanbepmoc.com.vn/?lang=en

Please find pictures and current menu attached.

If there are any items that you cannot find the pictures for please leave a space and we will add a picture into that slot.

Industry/Entity Type

Restaurant

```html
<!DOCTYPE html>
<html lang="en">
<head>
<meta charset="utf-8">
<title>Vietnamese Noodle Bar – Spices Spread</title>
<link rel="stylesheet" href="https://fonts.googleapis.com/css2?family=Playfair+Display:ital,wght@0,400;0,500;1,400;1,500&display=swap">
<style>
  :root {
    --paper: #ffffff;
    --ink-gold: #957a52;
    --sketch-tint: #f1ebe1;
    --spice-warm: #a27a5a;
    --spice-linen: #e9e4dc;
    --cinnamon: #9a5f42;
    --herb-green: #4f7a3a;
    --herb-purple: #4a3342;
  }
  * { margin: 0; padding: 0; box-sizing: border-box; }
  html, body { width: 1200px; height: 848px; overflow: hidden; background: var(--paper); }
  .spread {
    position: relative;
    width: 1200px;
    height: 848px;
    background: var(--paper);
    font-family: "Playfair Display", serif;
    color: var(--ink-gold);
  }

  /* botanical sketches, kept clear of the statement text */
  .sketch {
    position: absolute;
    background: var(--sketch-tint);
    border-radius: 4px;
  }
  .sketch--mint { left: 0; top: 0; width: 152px; height: 180px; }
  .sketch--tomato-garlic { left: 430px; top: 0; width: 154px; height: 200px; }
  .sketch--flowering-herb { left: 0; top: 585px; width: 172px; height: 263px; }
  .sketch--cinnamon-sprig { left: 334px; top: 612px; width: 266px; height: 236px; }

  /* statement */
  .statement {
    position: absolute;
    left: 0; top: 0;
    width: 600px; height: 848px;
  }
  .statement__rule {
    position: absolute;
    left: 274px;
    width: 53px;
    height: 2px;
    background: var(--ink-gold);
  }
  .statement__rule--top { top: 191px; }
  .statement__rule--bottom { top: 598px; }
  .statement__line {
    position: absolute;
    left: 0;
    width: 600px;
    text-align: center;
    white-space: nowrap;
    line-height: 1;
    font-weight: 400;
  }
  .statement__lead { top: 215px; font-size: 22px; }
  .statement__script {
    font-style: italic;
    font-weight: 400;
  }
  .statement__script--herbs { top: 224px; font-size: 92px; letter-spacing: 2.5px; }
  .statement__script--meats { top: 295px; left: 29px; font-size: 88px; letter-spacing: 1px; }
  .statement__script--meats .small { font-size: 54px; }
  .statement__middle { top: 402px; font-size: 22px; }
  .statement__headline {
    top: 430px;
    font-size: 66px;
    font-weight: 500;
    letter-spacing: 2.5px;
  }
  .statement__considered { top: 500px; font-size: 20px; letter-spacing: 1px; }
  .statement__claim { top: 520px; font-size: 30px; }
  .statement__world { top: 549px; font-size: 21px; letter-spacing: 0.8px; }

  /* photographs */
  .photo { position: absolute; }
  .photo--spice-pile {
    left: 632px; top: 30px; width: 364px; height: 545px;
    background: linear-gradient(160deg, var(--spice-linen) 0%, #c9aa82 40%, var(--spice-warm) 70%, #e6e0d6 100%);
  }
  .photo--cinnamon-stack {
    left: 1024px; top: 30px; width: 140px; height: 545px;
    background: linear-gradient(180deg, #5a3d30 0%, var(--cinnamon) 35%, #b9876a 70%, #8c5a44 100%);
  }
  .photo--spice-still {
    left: 632px; top: 610px; width: 186px; height: 203px;
    background: linear-gradient(150deg, #eeeeec 0%, #d8d4cf 50%, #9c7a63 100%);
  }
  .photo--herb-bunch {
    left: 853px; top: 610px; width: 311px; height: 203px;
    background: linear-gradient(120deg, #6f9e4e 0%, var(--herb-green) 45%, var(--herb-purple) 75%, #a99b8a 100%);
  }
</style>
</head>
<body>
<main class="spread">
  <div class="sketch sketch--mint" role="img" aria-label="Engraved line sketch of mint leaves"></div>
  <div class="sketch sketch--tomato-garlic" role="img" aria-label="Engraved line sketch of a halved tomato and garlic bulbs"></div>
  <div class="sketch sketch--flowering-herb" role="img" aria-label="Engraved line sketch of a flowering herb stem"></div>
  <div class="sketch sketch--cinnamon-sprig" role="img" aria-label="Engraved line sketch of cinnamon sticks, star anise and a herb sprig"></div>

  <section class="statement">
    <span class="statement__rule statement__rule--top"></span>
    <p class="statement__line statement__lead">WITH THE BALANCE BETWEEN</p>
    <p class="statement__line statement__script statement__script--herbs">fresh herbs</p>
    <p class="statement__line statement__script statement__script--meats"><span class="small">and</span> meats</p>
    <p class="statement__line statement__middle">AND A SELECTIVE USE OF SPICES TO REACH A</p>
    <h1 class="statement__line statement__headline">FINE TASTE,</h1>
    <p class="statement__line statement__considered">VIETNAMESE FOOD IS CONSIDERED</p>
    <p class="statement__line statement__claim">ONE OF THE HEALTHIEST CUISINES</p>
    <p class="statement__line statement__world">WORLWIDE</p>
    <span class="statement__rule statement__rule--bottom"></span>
  </section>

  <div class="photo photo--spice-pile" role="img" aria-label="Photo of star anise, cinnamon sticks, coriander seeds, cloves, dried chillies and spice sachets on linen"></div>
  <div class="photo photo--cinnamon-stack" role="img" aria-label="Close-up photo of stacked cinnamon sticks with star anise"></div>
  <div class="photo photo--spice-still" role="img" aria-label="Photo of cinnamon bark, star anise and seeds on a pale surface"></div>
  <div class="photo photo--herb-bunch" role="img" aria-label="Photo of fresh Thai basil, mint and purple perilla leaves"></div>
</main>
</body>
</html>
```